Menu Board For a Bubble Tea Trailer

Pearlwave is a bubble tea trailer that will be located in town and by the beach. Our aim is to bring refreshing beverages to our local community. My menu needs to reflect a bubbly and happy atmosphere of delicious fruit and some floral drinks, without looking unprofessional or childish.

My menu needs to be 1600mm long by 500mm high. It will be printed and attached to a sneeze guard for my beverage trailer which will be displayed on my serving window.

All drinks are priced as follows:
Regular: $6.50 Large: $7.50
Extra Topping: $0.60

Target Market(s)

Ages 15-39 including high school students, and young to middle aged workers that feel they need an energy or mood boost.

Industry/Entity Type

Bubble Tea (Non Alcoholic beverage)

Font styles to use
Sans Serif
Script

Colors
0094D4
00A9DD
6FCCEA
C7EBF8
E9F6FB
00AB8E
00BBA5
67D7C9
C6EFE9
E9F9F6
EE7325
F08F49
F5BC92
FAE3D3
FDF4ED
EB3D1F
EC4F4E
F09395
F8D3D4
FCEDEE

Requirements
Must have
• Pictures of bubble tea, Not crowded, easy to read, complimentary colours, prices, pictures must be in round bottom cups and without lid (attached)
Nice to have
• Bubbles or wave pattern
Should not have
• No black background, no fruits, no cartoon looking pictures

```html
<!DOCTYPE html>
<html lang="en">
<head>
<meta charset="utf-8">
<title>Pearlwave Menu Board</title>
<link rel="stylesheet" href="https://fonts.googleapis.com/css2?family=Itim&family=Lobster&family=Oswald:wght@500&family=Dosis:wght@500&display=swap">
<style>
  :root {
    --sky-deep: #00a9dd;
    --sky: #6fccea;
    --sky-soft: #c7ebf8;
    --sky-mist: #e9f6fb;
    --teal: #00bba5;
    --teal-deep: #00ab8e;
    --teal-soft: #67d7c9;
    --coral: #ec4f4e;
    --coral-soft: #f09395;
    --crimson: #c8102e;
    --ink: #1c1c1c;
    --leaf: #4aa02c;
    --leaf-deep: #2f7a1c;
    --white: #ffffff;
  }
  * { box-sizing: border-box; margin: 0; padding: 0; }
  html, body { width: 1070px; height: 1200px; overflow: hidden; background: var(--white); }
  .canvas { position: relative; width: 1070px; height: 1200px; }
  .menu-board {
    position: absolute; left: 20px; top: 439px; width: 1030px; height: 322px; overflow: hidden;
    background:
      radial-gradient(ellipse 45% 55% at 52% 48%, rgba(255,255,255,0.95), rgba(255,255,255,0) 100%),
      linear-gradient(180deg, var(--sky) 0%, var(--sky-soft) 45%, var(--sky-mist) 100%);
    box-shadow: 0 10px 24px rgba(0,0,0,0.18);
    font-family: "Itim", sans-serif; color: var(--ink);
  }
  .art { position: absolute; }
  .art--drink-splash { left: 0; top: 0; width: 290px; height: 322px;
    background:
      radial-gradient(ellipse 60% 70% at 40% 65%, rgba(74,160,44,0.95), rgba(74,160,44,0.55) 60%, rgba(74,160,44,0) 100%),
      radial-gradient(ellipse 30% 25% at 62% 14%, rgba(255,255,255,0.7), rgba(255,255,255,0) 100%); }
  .art--ice { left: 250px; bottom: 0; width: 780px; height: 60px;
    background: linear-gradient(180deg, rgba(199,235,248,0) 0%, rgba(111,204,234,0.45) 100%); }
  .art--leaves { top: 0; height: 30px; background: radial-gradient(ellipse 50% 100% at 50% 0, rgba(74,160,44,0.75), rgba(74,160,44,0) 100%); }
  .art--soft { border-radius: 50%; }
  .art--mixed-berries { left: 416px; top: 26px; width: 64px; height: 48px;
    background: radial-gradient(ellipse at 55% 50%, rgba(240,143,73,0.7), rgba(63,95,176,0.45) 55%, rgba(63,95,176,0) 100%); }
  .art--mango-berries { left: 690px; top: 84px; width: 60px; height: 40px;
    background: radial-gradient(ellipse at 50% 50%, rgba(236,79,78,0.7), rgba(245,188,146,0.45) 55%, rgba(245,188,146,0) 100%); }
  .art--cherries { left: 918px; top: 46px; width: 36px; height: 36px;
    background: radial-gradient(ellipse at 50% 60%, rgba(217,43,43,0.7), rgba(217,43,43,0) 100%); }
  .art--watermelon { left: 206px; top: 199px; width: 68px; height: 56px;
    background: radial-gradient(ellipse at 50% 55%, rgba(233,68,68,0.65), rgba(47,122,28,0.45) 55%, rgba(47,122,28,0) 100%); }
  .art--banana { left: 360px; top: 250px; width: 100px; height: 62px;
    background: radial-gradient(ellipse at 45% 50%, rgba(247,209,74,0.75), rgba(247,209,74,0.35) 55%, rgba(247,209,74,0) 100%); }
  .art--fruit-cup { left: 948px; top: 146px; width: 82px; height: 176px;
    background: radial-gradient(ellipse 50% 55% at 50% 55%, rgba(236,79,78,0.65), rgba(248,211,212,0.45) 60%, rgba(248,211,212,0) 100%); }
  .art--lemon { left: 900px; top: 276px; width: 54px; height: 44px;
    background: radial-gradient(ellipse at 50% 50%, rgba(247,209,74,0.7), rgba(247,209,74,0) 100%); }

  .section-tag { position: absolute; height: 30px; border-radius: 15px 6px 15px 6px;
    font-family: "Lobster", cursive; font-weight: 400; color: var(--white); font-size: 21px; line-height: 30px; padding-left: 14px; }
  .section-tag--milk { left: 282px; top: 50px; width: 126px; background: var(--coral); }
  .section-tag--tea { left: 510px; top: 50px; width: 206px; background: var(--teal); }
  .section-tag--toppings { left: 786px; top: 46px; width: 126px; background: var(--coral); font-size: 22px; }

  .item-list { position: absolute; list-style: none; font-size: 13.5px; line-height: 20.5px; }
  .item-list--milk-a { left: 288px; top: 98px; }
  .item-list--milk-b { left: 401px; top: 98px; }
  .item-list--tea-a { left: 520px; top: 98px; }
  .item-list--tea-b { left: 630px; top: 98px; }
  .item-list--popping { left: 746px; top: 130px; width: 120px; text-align: center; }
  .item-list--jelly { left: 866px; top: 132px; width: 100px; text-align: center; }

  .topping-title { position: absolute; left: 776px; top: 81px; width: 140px; text-align: center;
    font-family: "Dosis", sans-serif; font-size: 16px; }
  .topping-kind { position: absolute; font-family: "Lobster", cursive; font-weight: 400; font-size: 13px; text-align: center; }
  .topping-kind--popping { left: 746px; top: 110px; width: 120px; color: var(--teal-deep); }
  .topping-kind--jelly { left: 866px; top: 112px; width: 100px; color: var(--crimson); }

  .price-banner { position: absolute; left: 489px; top: 212px; width: 266px; height: 27px;
    background: var(--coral); color: var(--white); font-family: "Oswald", sans-serif; font-size: 15px;
    letter-spacing: 1px; line-height: 27px; text-align: center; }
  .price-row { position: absolute; font-family: "Oswald", sans-serif; font-size: 15px; line-height: 22px; display: flex; align-items: center; gap: 10px; }
  .price-row--sizes { left: 499px; top: 246px; }
  .price-row--topping { left: 540px; top: 276px; }
  .price-row .gap { width: 14px; }
  .price-tag { display: inline-block; background: var(--teal); color: var(--white); border-radius: 6px 3px 6px 3px; padding: 0 6px; font-size: 15px; line-height: 22px; }
</style>
</head>
<body>
<div class="canvas">
  <section class="menu-board" aria-label="Pearlwave bubble tea menu">
    <div class="art art--ice" role="img" aria-label="Ice cubes along the bottom edge"></div>
    <div class="art art--leaves" style="left:0;width:70px" role="img" aria-label="Green leaves"></div>
    <div class="art art--leaves" style="left:470px;width:90px" role="img" aria-label="Green leaves"></div>
    <div class="art art--leaves" style="left:640px;width:50px" role="img" aria-label="Green leaves"></div>
    <div class="art art--leaves" style="left:975px;width:55px" role="img" aria-label="Green leaves"></div>
    <div class="art art--drink-splash" role="img" aria-label="Green matcha bubble tea with pearls, ice and a straw splashing"></div>
    <div class="art art--soft art--watermelon" role="img" aria-label="Watermelon slice"></div>
    <div class="art art--soft art--mixed-berries" role="img" aria-label="Orange slice and blueberries"></div>
    <div class="art art--soft art--mango-berries" role="img" aria-label="Mango and red berries"></div>
    <div class="art art--soft art--cherries" role="img" aria-label="Cherries"></div>
    <div class="art art--soft art--banana" role="img" aria-label="Banana, blueberries and strawberry"></div>
    <div class="art art--soft art--fruit-cup" role="img" aria-label="Pink fruit tea with pearls in a cup"></div>
    <div class="art art--soft art--lemon" role="img" aria-label="Lemon and strawberry"></div>

    <h2 class="section-tag section-tag--milk">Milk Tea</h2>
    <ul class="item-list item-list--milk-a"><li>Thai</li><li>Royal</li><li>Original</li><li>Tiger Pearl</li><li>Young Coconut</li><li>Watermelon</li><li>Banana</li></ul>
    <ul class="item-list item-list--milk-b"><li>Taro</li><li>Lychee</li><li>Honeydew</li><li>Strawberry</li><li>Lavender</li><li>Mango</li><li>Rose</li></ul>

    <h2 class="section-tag section-tag--tea">Green Tea / Red Tea</h2>
    <ul class="item-list item-list--tea-a"><li>Peach</li><li>Mango</li><li>Passionfruit</li><li>Watermelon</li><li>Dragonfruit</li></ul>
    <ul class="item-list item-list--tea-b"><li>Grape</li><li>Lychee</li><li>strawberry</li><li>Green Apple</li><li>Pomegranate</li></ul>

    <h2 class="section-tag section-tag--toppings">Toppings</h2>
    <p class="topping-title">Tapioca Pearls</p>
    <h3 class="topping-kind topping-kind--popping">Popping Pearls</h3>
    <ul class="item-list item-list--popping"><li>Peach</li><li>Mango</li><li>Lychee</li><li>Strawberry</li><li>Passionfruit</li><li>Watermelon</li></ul>
    <h3 class="topping-kind topping-kind--jelly">Fruit Jelly</h3>
    <ul class="item-list item-list--jelly"><li>Rainbow</li><li>Lychee</li><li>Mango</li><li>Peach</li><li>Grape</li></ul>

    <p class="price-banner">ALL DRINKS ARE PRICED AS FOLLOWS</p>
    <p class="price-row price-row--sizes">REGULAR <span class="price-tag">$6.50</span><span class="gap"></span>LARGE <span class="price-tag">$7.50</span></p>
    <p class="price-row price-row--topping">EXTRA TOPPING <span class="price-tag">$0.60</span></p>
  </section>
</div>
</body>
</html>
```